Business Card for premium dental clinic

We are a premium dental clinic based in Brasov, Romania with more than 15 year on the market, providing quality dental treatment made by a team of more specialized dentists, working with modern equipment as a solution to beautiful and healthy teeth.

Our current logo for the clinic use 2 square with colors black and gold - dr Corbescu - studio, using family fonts Bodoni, Myriad Pro and Segoe Print.
Depending on the printing we used some gold CMYK background or gold foil picture background or a gold gradient.
We want a business card:
- eye catching business card
- distinguished business card
- premium design
- to keep the color scheme of black and gold
- to attract the customers to spent time reading the information
- modern concept

```html
<!DOCTYPE html>
<html lang="en">
<head>
<meta charset="utf-8">
<title>Lumen Dental Clinic – Business Card</title>
<link rel="stylesheet" href="https://fonts.googleapis.com/css2?family=Encode+Sans+Condensed:wght@300;400&family=Montserrat:wght@300;400;500&display=swap">
<style>
  :root {
    --backdrop: #2a2a2b;
    --card-black: #0b0b0b;
    --ink-white: #ffffff;
    --gold-deep: #c98a1e;
    --gold-mid: #e6b83a;
    --gold-light: #f5e25e;
    --gold-text: #f2c230;
    --arc-grey: #2c2c2e;
  }
  * { box-sizing: border-box; margin: 0; padding: 0; }
  html, body { width: 1200px; height: 900px; overflow: hidden; }
  body {
    background: var(--backdrop);
    font-family: "Montserrat", Arial, sans-serif;
    position: relative;
  }
  .card {
    position: absolute;
    left: 250px;
    width: 700px;
    height: 400px;
    background: var(--card-black);
    overflow: hidden;
    box-shadow: 0 10px 30px rgba(0,0,0,.45);
  }
  .card--front { top: 40px; }
  .card--back { top: 470px; }

  /* Front */
  .front-frame {
    position: absolute;
    left: 110px; top: 68px;
    width: 540px; height: 222px;
    border: 2px solid var(--ink-white);
  }
  .gold-foil {
    position: absolute;
    left: 0; top: 0;
    width: 260px; height: 100%;
    background: radial-gradient(ellipse at 35% 40%, #f7d45a 0%, #e2ac2c 45%, #c58a18 80%, #a8700f 100%);
  }
  .name-plate {
    position: absolute;
    left: 60px; top: 96px;
    width: 250px; height: 74px;
    background: var(--ink-white);
    display: flex; align-items: center; justify-content: center;
  }
  .doctor-name {
    font-family: "Encode Sans Condensed", "Arial Narrow", sans-serif;
    font-weight: 300;
    color: #111;
    font-size: 40px;
    letter-spacing: .5px;
    white-space: nowrap;
  }
  .doctor-name small { font-size: 24px; }
  .brand {
    position: absolute;
    right: 24px; top: 50px;
    text-align: right;
    color: var(--ink-white);
    font-family: "Montserrat", Arial, sans-serif;
    font-weight: 400;
  }
  .brand__name { font-size: 40px; line-height: 1; }
  .brand__tag { font-size: 19px; margin-top: 42px; }
  .front-web {
    position: absolute;
    left: 0; right: 0; top: 318px;
    text-align: center;
    color: var(--ink-white);
    font-size: 18px;
    font-weight: 300;
    letter-spacing: 1px;
  }
  .front-web strong { color: var(--gold-text); font-weight: 500; }

  /* Back */
  .back-arc { position: absolute; inset: 0; }
  .gold-band {
    position: absolute;
    left: 0; bottom: 0;
    width: 100%; height: 200px;
    background: linear-gradient(100deg, var(--gold-deep) 0%, var(--gold-mid) 35%, var(--gold-light) 60%, var(--gold-mid) 100%);
  }
  .logo-square {
    position: absolute;
    left: 65px; top: 50px;
    width: 170px; height: 170px;
    background: var(--card-black);
    border: 4px solid var(--gold-mid);
    color: var(--ink-white);
    text-align: right;
    padding: 40px 12px 0 0;
  }
  .logo-square .brand__name { font-size: 30px; }
  .logo-square .brand__tag { font-size: 14px; margin-top: 38px; }
  .name-outline {
    position: absolute;
    left: 80px; top: 275px;
    width: 220px; height: 66px;
    border: 1.5px solid var(--ink-white);
    display: flex; align-items: center; justify-content: center;
  }
  .name-outline .doctor-name { color: var(--ink-white); font-size: 36px; }
  .name-outline .doctor-name small { font-size: 22px; }
  .divider {
    position: absolute;
    left: 380px; top: 240px;
    width: 1.5px; height: 120px;
    background: rgba(255,255,255,.8);
  }
  .contacts {
    position: absolute;
    left: 420px; top: 242px;
    list-style: none;
    color: var(--ink-white);
    font-size: 16px;
    font-weight: 400;
  }
  .contacts li { display: flex; align-items: center; gap: 12px; height: 28px; }
  .contacts svg { width: 16px; height: 16px; flex: none; }
</style>
</head>
<body>
  <section class="card card--front">
    <div class="front-frame">
      <div class="gold-foil" role="img" aria-label="Crumpled gold foil texture"></div>
      <div class="brand">
        <div class="brand__name">Lumen</div>
        <div class="brand__tag">dental clinic</div>
      </div>
    </div>
    <div class="name-plate"><span class="doctor-name"><small>dr.</small>Corbescu</span></div>
    <p class="front-web">info.<strong>lumendental</strong>.com</p>
  </section>

  <section class="card card--back">
    <svg class="back-arc" viewBox="0 0 700 400" aria-hidden="true">
      <path d="M250 400 C 300 170, 520 70, 690 120" fill="none" stroke="var(--arc-grey)" stroke-width="22" stroke-linecap="round"/>
    </svg>
    <div class="gold-band"></div>
    <div class="logo-square">
      <div class="brand__name">Lumen</div>
      <div class="brand__tag">dental clinic</div>
    </div>
    <div class="name-outline"><span class="doctor-name"><small>dr.</small>Corbescu</span></div>
    <div class="divider"></div>
    <ul class="contacts">
      <li>
        <svg viewBox="0 0 16 16" fill="none" stroke="#fff" stroke-width="1.4"><path d="M4 2 L6 5 L5 7 Q7 10 9 11 L11 10 L14 12 L12 14.5 Q4 13 1.5 4 Z"/></svg>
        +00 000 481 5520
      </li>
      <li>
        <svg viewBox="0 0 16 16" fill="none" stroke="#fff" stroke-width="1.4"><rect x="4.5" y="1.5" width="7" height="13" rx="1.2"/><line x1="7" y1="12" x2="9" y2="12"/></svg>
        +00 000 481 5520
      </li>
      <li>
        <svg viewBox="0 0 16 16" fill="none" stroke="#fff" stroke-width="1.4"><rect x="1.5" y="3.5" width="13" height="9"/><path d="M1.5 3.5 L8 9 L14.5 3.5"/></svg>
        info@lumendental.com
      </li>
    </ul>
  </section>
</body>
</html>
```